Furniture protector Packaging insert

Hello,

I am looking to redesign a packaging insert for a sofa silpcover . I will give you all the details of what the sofa slipcover intentions are for and and I would like you to include these on the insert...Background colors should be a mix of 2 colors and more of a settle colors - please do not use blue , red, orange , green, pink , purple , violet, yellow, turq...

Industry/Entity Type

Furniture

Requirements
Must have
• -Please revise from New and Improved to a different wording
-Please use all reasons of what item is made for...
-Please make sure to include the water repellent logo (can make own logo)
-Please include sizes of slipcover with a small box for a check next to each size
-Chair: 65" x 70.5+ 5 inch drop
-Loveseat:88" x 70.5 + 5 inch drop
-Sofa: 110" x 70.5 + 5 inch drop
-Please include the colors for each size (brown, burg, camel, Gray)
-Picture must be included on the packaging insert
-Packaging insert size should be the same as is ( please look at the attached insert to redesign)
-Must Have SKU / barcode
-Fill , Fabric and Care must be on the insert
-Please use my TVR.QO logo - Company logo does not have to be in purple ...
-Please use logo of 5 inch drop - can be changed or add some touch up or colors...
-Please include RN number , country of origin and color name..
Should not have
• -please do not use blue , red, orange , green, pink , purple , violet, yellow, turq... for background colors or for an column or wording.
-Please use normal and simple fonts...Fonts can be different for any purpose you may have.

```html
<!DOCTYPE html>
<html lang="en">
<head>
<meta charset="utf-8">
<title>Furniture Protector – Packaging Insert</title>
<link rel="stylesheet" href="https://fonts.googleapis.com/css2?family=Oswald:wght@700&family=Roboto+Condensed:wght@400;700&family=Arimo:wght@700&display=swap">
<style>
  :root{
    --taupe-deep:#4f4336;
    --taupe:#6e604f;
    --taupe-light:#9a8a72;
    --camel:#b89a6e;
    --sand:#d9c7a3;
    --cream:#fbf8ef;
    --cream-line:#eee8d4;
    --accent:#7a4e2d;
    --ink:#1d1d1b;
    --white:#ffffff;
  }
  *{margin:0;padding:0;box-sizing:border-box}
  html,body{width:1200px;height:1120px;overflow:hidden;background:var(--taupe)}
  .insert{position:relative;width:1200px;height:1120px;overflow:hidden;font-family:"Roboto Condensed",sans-serif}
  .backdrop{position:absolute;inset:0}
  .headline{position:absolute;left:110px;top:78px;font-family:"Oswald",sans-serif;font-weight:700;font-size:54px;line-height:1;color:var(--white);letter-spacing:0;text-shadow:2px 2px 0 rgba(0,0,0,.4)}
  .brand{position:absolute;left:866px;top:50px;display:flex;align-items:center;gap:10px}
  .brand-mark{width:26px;height:26px;background:var(--ink)}
  .brand-name{font-family:"Arimo",sans-serif;font-weight:700;font-size:48px;line-height:1;color:var(--ink);letter-spacing:1px}
  .title{position:absolute;right:46px;font-family:"Arimo",sans-serif;font-weight:700;line-height:1;text-align:right;font-size:60px}
  .title-accent{top:120px;color:var(--accent)}
  .title-black{top:184px;color:var(--ink)}
  .features{position:absolute;left:64px;top:214px;list-style:none;width:340px}
  .features li{position:relative;padding-left:38px;color:var(--white);font-size:23px;line-height:28px;margin-bottom:11px}
  .features li::before{content:"";position:absolute;left:0;top:8px;width:12px;height:12px;background:var(--white)}
  .size-tag{position:absolute;left:0;width:300px;height:76px;background:var(--white);border-radius:0 38px 38px 0;box-shadow:0 6px 0 #3a3128;padding:6px 0 0 62px}
  .size-tag .check{position:absolute;left:20px;top:24px;width:26px;height:26px;border:3px solid var(--taupe-deep);background:var(--white)}
  .size-tag .name{display:block;font-family:"Arimo",sans-serif;font-weight:700;font-size:22px;line-height:25px;color:var(--accent)}
  .size-tag .dims{display:block;font-family:"Arimo",sans-serif;font-weight:700;font-size:15px;line-height:19px;color:var(--ink)}
  .size-tag .colors{display:block;font-size:14px;line-height:18px;color:var(--taupe)}
  .photo-frame{position:absolute;left:424px;top:264px;width:716px;height:648px;background:var(--white);border-radius:22px;box-shadow:0 0 10px rgba(0,0,0,.25)}
  .photo{position:absolute;left:10px;top:10px;width:696px;height:628px;border-radius:16px;background:linear-gradient(160deg,#e9d6b4 0%,#c8a882 40%,#8a7a5a 70%,#a08e6a 100%)}
  .circle{position:absolute;border-radius:50%;border:4px solid var(--white);overflow:hidden}
  .circle-photo{left:572px;top:738px;width:260px;height:260px;background:linear-gradient(170deg,#d8c6a4 0%,#9a8660 55%,#b9a680 100%)}
  .circle-diagram{left:854px;top:736px;width:264px;height:264px;background:var(--white)}
  .diagram-art{position:absolute;left:40px;top:38px;width:184px;height:100px;background:#efeeea;border-radius:8px}
  .diagram-note{position:absolute;left:0;right:0;top:164px;text-align:center;font-size:15px;line-height:19px;color:#333}
  .info-band{position:absolute;left:0;top:996px;width:1200px;height:124px}
  .badge{position:absolute;left:0;top:0;width:228px;height:124px;background:var(--white);border-radius:0 34px 0 0}
  .badge-icon{position:absolute;left:38px;top:20px;width:68px;height:68px}
  .badge-text{position:absolute;left:114px;top:20px;font-family:"Arimo",sans-serif;font-weight:700;font-size:19px;line-height:22px;color:var(--ink)}
  .spec{position:absolute;top:22px;text-align:center;color:var(--ink);font-size:15.5px;line-height:19.5px}
  .spec h3{font-family:"Arimo",sans-serif;font-weight:700;font-size:15px;line-height:19px}
  .spec-fill{left:238px;width:160px}
  .spec-fabric{left:432px;width:230px}
  .spec-care{left:676px;width:280px}
  .origin{position:absolute;left:968px;top:0;width:232px;height:124px;background:var(--white);border-radius:34px 0 0 0;padding:16px 0 0 40px;font-family:"Arimo",sans-serif;font-weight:700;font-size:15px;line-height:18px;color:var(--ink)}
  .origin .sku{display:block;margin-top:2px;color:var(--accent)}
</style>
</head>
<body>
<main class="insert">
  <svg class="backdrop" width="1200" height="1120" viewBox="0 0 1200 1120" aria-hidden="true">
    <defs>
      <linearGradient id="ground" x1="0" y1="0" x2="0.4" y2="1">
        <stop offset="0" stop-color="#5a4d3e"/>
        <stop offset="0.55" stop-color="#6e604f"/>
        <stop offset="1" stop-color="#8c7c66"/>
      </linearGradient>
      <linearGradient id="arrow" x1="0" y1="0" x2="1" y2="0">
        <stop offset="0" stop-color="#4f4336"/>
        <stop offset="0.55" stop-color="#8a7258"/>
        <stop offset="1" stop-color="#c2a67c"/>
      </linearGradient>
      <pattern id="stripes" width="8" height="8" patternUnits="userSpaceOnUse">
        <rect width="8" height="8" fill="#fbf8ef"/>
        <rect width="8" height="3" fill="#eee8d4"/>
      </pattern>
    </defs>
    <rect width="1200" height="1120" fill="url(#ground)"/>
    <path d="M560 0 Q520 140 600 264 L560 264 Q470 130 520 0 Z" fill="#d9c7a3"/>
    <path d="M600 0 H1200 V600 Q1150 608 1130 630 L620 630 L620 264 Q560 140 600 0 Z" fill="url(#stripes)"/>
    <path d="M0 0 H610 L742 102 L650 184 L660 150 Q380 232 0 156 Z" fill="#2e261e" opacity="0.45" transform="translate(6 14)"/>
    <path d="M0 0 H600 L728 96 L640 176 L650 144 Q380 226 0 150 Z" fill="url(#arrow)"/>
    <rect x="0" y="996" width="1200" height="124" fill="url(#stripes)"/>
  </svg>

  <h1 class="headline">Everyday Protection</h1>

  <div class="brand">
    <span class="brand-mark"></span>
    <span class="brand-name">TVR.QO</span>
  </div>
  <h2 class="title title-accent">FURNITURE</h2>
  <h2 class="title title-black">PROTECTOR</h2>

  <ul class="features">
    <li>Protects Furniture from Kids, Pets and more.</li>
    <li>Quilted Microfiber Water Repellent Finish</li>
    <li>Longer over back</li>
    <li>Soil Resistant</li>
    <li>Machine Washable</li>
    <li>Snag Resistant</li>
    <li>Easy to install on &amp; off in a Flash</li>
    <li>Fits More Types of Furniture Styles.</li>
  </ul>

  <div class="size-tag" style="top:700px"><span class="check"></span><span class="name">LOVESEAT</span><span class="dims">88" X 70.5" + 5" DROP</span><span class="colors">Brown · Burg · Camel · Gray</span></div>
  <div class="size-tag" style="top:786px"><span class="check"></span><span class="name">CHAIR</span><span class="dims">65" X 70.5" + 5" DROP</span><span class="colors">Brown · Burg · Camel · Gray</span></div>
  <div class="size-tag" style="top:872px"><span class="check"></span><span class="name">SOFA</span><span class="dims">110" X 70.5" + 5" DROP</span><span class="colors">Brown · Burg · Camel · Gray</span></div>

  <div class="photo-frame">
    <div class="photo" role="img" aria-label="Living room photo: a quilted protector on a loveseat with a child and a dog sitting on it"></div>
  </div>

  <div class="circle circle-photo" role="img" aria-label="Photo of a loveseat fully covered by the quilted protector"></div>
  <div class="circle circle-diagram">
    <div class="diagram-art" role="img" aria-label="Line drawing showing the protector's 5 inch drop tucked into three sides of the seat"></div>
    <p class="diagram-note">5 inch drop should tuck into 3 sides<br>of the furniture , as shown here.</p>
  </div>

  <section class="info-band">
    <div class="badge">
      <svg class="badge-icon" viewBox="0 0 68 68" aria-hidden="true">
        <rect x="1" y="1" width="66" height="66" rx="5" fill="#6e604f" stroke="#1d1d1b" stroke-width="2"/>
        <path d="M34 10 C26 24 18 32 18 42 A16 16 0 0 0 50 42 C50 32 42 24 34 10 Z" fill="#ffffff"/>
        <path d="M34 18 C29 28 24 34 24 42 A10 10 0 0 0 44 42 C44 34 39 28 34 18 Z" fill="#d9c7a3"/>
      </svg>
      <p class="badge-text">Water<br>Repellent<br>Finish</p>
    </div>
    <div class="spec spec-fill">
      <h3>FILL :</h3>
      <p>100% polysterfiberfill<br>100%polyester fiberfill<br>100%poliester fiberfill</p>
    </div>
    <div class="spec spec-fabric">
      <h3>FABRIC :</h3>
      <p>100% Sueded polyester microfiber<br>100% Sueded polyester microfiber<br>100% Suede poliester microfiber</p>
    </div>
    <div class="spec spec-care">
      <h3>CARE :</h3>
      <p>Machine washable. See sewn in label<br>Machine lavable Voir letiquette de soin<br>Maquina lavable.&nbsp; er la etiqueta del cuidado</p>
    </div>
    <div class="origin">Colar : Sage<br>Country of Origin :<br>China<br>RN 148302<span class="sku">SKU : TQ-FP-0100</span></div>
  </section>
</main>
</body>
</html>
```